Brambleton Chiropractic. We have two locations that we want to advertise on the same card. Kelwin MotionCare campus address: 3815 Tamsey Rd., Suite 240, Flowood, MS 39987. Madison address: 428 Pellham Ct., Building D., Madison, MS 39974. website: www.drbrambleton-example.com. o:(601)555-0147 f:(601)555-0183

Target Market(s)

Health care decision makers: primary care doctors and mothers

Contact Information for Business Card

I have no idea; up for any suggestions and I'd do much better picking from examples versus describing what I'm looking for. We are in a very high end location and would like the cards to look really sharp.

Requirements
Must have
• My name, Marcus L Denbrook, D.C.

```html
<!DOCTYPE html>
<html lang="en">
<head>
<meta charset="utf-8">
<title>Brambleton Chiropractic – Business Card</title>
<link rel="stylesheet" href="https://fonts.googleapis.com/css2?family=Cinzel:wght@500&family=Open+Sans:wght@400;600&display=swap">
<style>
  :root {
    --backdrop: #e3e3e3;
    --ink: #0b0b0b;
    --paper: #fbfbfb;
    --on-dark: #f2f2f2;
    --on-dark-muted: #bdbdbd;
    --line-dark: #d8d8d8;
  }
  * { margin: 0; padding: 0; box-sizing: border-box; }
  html, body { width: 1200px; height: 801px; overflow: hidden; }
  body {
    background: var(--backdrop);
    font-family: "Open Sans", Arial, sans-serif;
    position: relative;
  }
  .card {
    position: absolute;
    top: 252px;
    width: 525px;
    height: 300px;
    box-shadow: 0 6px 18px rgba(0,0,0,0.12);
  }
  .card--back { left: 55px; background: var(--ink); color: var(--on-dark); }
  .card--front { left: 620px; background: var(--paper); color: var(--ink); }

  /* wordmark */
  .wordmark {
    font-family: "Cinzel", Georgia, serif;
    font-weight: 500;
    line-height: 1;
    display: flex;
    align-items: center;
    gap: 12px;
  }
  .wordmark__dot {
    border-radius: 50%;
    flex: none;
  }
  .wordmark__text { display: flex; flex-direction: column; }

  /* back card */
  .card--back .wordmark {
    position: absolute; left: 30px; top: 108px; color: var(--on-dark);
  }
  .card--back .wordmark__dot { width: 26px; height: 26px; border: 1.5px solid var(--on-dark); }
  .card--back .wordmark__name { font-size: 25px; letter-spacing: 0.5px; }
  .card--back .wordmark__sub { font-size: 15px; letter-spacing: 1px; margin-top: 2px; }

  .holder { position: absolute; left: 30px; top: 172px; }
  .holder__name { font-size: 17px; font-weight: 600; letter-spacing: 0.5px; text-transform: uppercase; }
  .holder__role { font-size: 10px; color: var(--on-dark-muted); margin-left: 34px; }

  .contact { position: absolute; left: 30px; top: 212px; display: flex; gap: 8px; }
  .contact__icons {
    width: 16px; background: var(--on-dark); border-radius: 3px;
    display: flex; flex-direction: column; justify-content: space-around; align-items: center;
    padding: 3px 0;
  }
  .contact__icons svg { width: 10px; height: 10px; }
  .contact__list { list-style: none; font-size: 11px; line-height: 15px; color: var(--on-dark); }

  .locations {
    position: absolute; right: 24px; top: 30px;
    display: flex; gap: 10px;
  }
  .locations__list { text-align: right; font-size: 11px; line-height: 15px; }
  .location + .location { margin-top: 8px; }
  .location__title { font-weight: 600; }
  .locations__rule { width: 2px; background: var(--line-dark); }

  /* front card */
  .card--front .wordmark {
    position: absolute; left: 50%; top: 50%; transform: translate(-50%, -50%);
    color: var(--ink); gap: 16px;
  }
  .card--front .wordmark__dot { width: 40px; height: 40px; border: 2px solid var(--ink); }
  .card--front .wordmark__name { font-size: 34px; letter-spacing: 0.5px; }
  .card--front .wordmark__sub { font-size: 21px; letter-spacing: 1.5px; margin-top: 3px; }
</style>
</head>
<body>

<section class="card card--back" aria-label="Business card, contact side">
  <div class="wordmark">
    <span class="wordmark__dot"></span>
    <div class="wordmark__text">
      <span class="wordmark__name">BRAMBLETON</span>
      <span class="wordmark__sub">CHIROPRACTIC</span>
    </div>
  </div>

  <div class="holder">
    <p class="holder__name">Marcus L Denbrook, DC</p>
    <p class="holder__role">Director</p>
  </div>

  <div class="contact">
    <div class="contact__icons">
      <svg viewBox="0 0 10 10" aria-hidden="true"><path d="M2 1l2 2-1 1.2q1 1.8 2.8 2.8L7 6l2 2-1.3 1.3Q4.5 9 1 2.3z" fill="#0b0b0b"/></svg>
      <svg viewBox="0 0 10 10" aria-hidden="true"><rect x="1" y="3" width="8" height="5" fill="#0b0b0b"/><rect x="3" y="1" width="4" height="2" fill="#0b0b0b"/></svg>
      <svg viewBox="0 0 10 10" aria-hidden="true"><rect x="1" y="2" width="8" height="6" fill="#0b0b0b"/><path d="M1 2l4 3.5L9 2" stroke="#f2f2f2" stroke-width="0.8" fill="none"/></svg>
      <svg viewBox="0 0 10 10" aria-hidden="true"><circle cx="5" cy="5" r="4" fill="none" stroke="#0b0b0b" stroke-width="1.2"/><path d="M1 5h8M5 1q-2 4 0 8M5 1q2 4 0 8" stroke="#0b0b0b" stroke-width="0.8" fill="none"/></svg>
    </div>
    <ul class="contact__list">
      <li>(601)555-0147</li>
      <li>(601)555-0183</li>
      <li>bwcmarcus@example.com</li>
      <li>www.drbrambleton-example.com</li>
    </ul>
  </div>

  <div class="locations">
    <div class="locations__list">
      <div class="location">
        <p class="location__title">Kelwin MotionCare campus:</p>
        <p>3815 Tamsey Rd., Suite 240</p>
        <p>Flowood, MS 39987</p>
      </div>
      <div class="location">
        <p class="location__title">Madison:</p>
        <p>428 Pellham Ct., Building D.</p>
        <p>Madison, MS 39974</p>
      </div>
    </div>
    <span class="locations__rule"></span>
  </div>
</section>

<section class="card card--front" aria-label="Business card, logo side">
  <div class="wordmark">
    <span class="wordmark__dot"></span>
    <div class="wordmark__text">
      <span class="wordmark__name">BRAMBLETON</span>
      <span class="wordmark__sub">CHIROPRACTIC</span>
    </div>
  </div>
</section>

</body>
</html>
```